Professional violinist needs business cards

I am trying to attract the following jobs:
-private violin lessons (primarily classical)
-performance gigs (weddings, birthday parties, funerals, etc.)
-collaborations with other artists (studio recordings, performances)

I want to communicate that I have a very high standard of excellence for my work, but I also love people and celebrations.
Values/style words I like are:
love, joy, peace, fun, beauty, authenticity, excellence, warmth, refined/sleek, free spirited. If that's too confusing, just ignore :)

I will attach my favorite business card template that I could find on Canva. The lines are supposed to be like a music staff, which I think is really cool, but I also don't want it to look too busy. I like the simple black and white--I think it looks sharp--but I also am open to other ideas. I also have seen business cards with pictures included that looked great, so I attached an image that could be used as well.

I am also attaching a file that I made of my initials that could be used as a logo, but I'm not sure if it should be included.

Information on the card:
-My name (18 letters total)
-"violinist"
-phone number, email, website

Thank you!

```html
<!DOCTYPE html>
<html lang="en">
<head>
<meta charset="utf-8">
<title>Violinist Business Cards</title>
<link href="https://fonts.googleapis.com/css2?family=Cormorant+Garamond:wght@500&display=swap" rel="stylesheet">
<style>
  :root {
    --backdrop: #1b1b1c;
    --card: #232323;
    --ink: #f2f2f0;
    --ink-soft: #d9d9d6;
    --staff-line: rgba(255, 255, 255, 0.78);
    --photo-warm: #7a6a50;
    --photo-deep: #3e352a;
    --photo-light: #a49577;
  }

  html, body {
    margin: 0;
    padding: 0;
    width: 1200px;
    height: 800px;
    overflow: hidden;
    background: var(--backdrop);
  }

  .canvas {
    position: relative;
    width: 1200px;
    height: 800px;
    font-family: "Cormorant Garamond", "Times New Roman", serif;
    font-weight: 500;
    color: var(--ink);
  }

  .card {
    position: absolute;
    width: 525px;
    height: 300px;
    background: var(--card);
    overflow: hidden;
    box-shadow: 0 6px 18px rgba(0, 0, 0, 0.45);
  }

  /* Front: portrait + contact details */
  .card--front {
    left: 90px;
    top: 90px;
  }

  .portrait {
    position: absolute;
    left: 0;
    top: 18px;
    bottom: 0;
    width: 218px;
    background: linear-gradient(160deg, var(--photo-light) 0%, var(--photo-warm) 45%, var(--photo-deep) 100%);
  }

  .contact {
    position: absolute;
    left: 250px;
    top: 58px;
    right: 16px;
    text-transform: uppercase;
  }

  .contact__name {
    margin: 0;
    font-size: 22px;
    letter-spacing: 0.12em;
    font-weight: 500;
    line-height: 1.1;
  }

  .contact__role {
    margin: 2px 0 0 18px;
    font-size: 15px;
    letter-spacing: 0.12em;
    line-height: 1.2;
  }

  .contact__rule {
    width: 18px;
    height: 1px;
    margin: 8px 0 6px 18px;
    background: var(--ink);
  }

  .contact__list {
    list-style: none;
    margin: 0;
    padding: 0 0 0 18px;
    text-transform: none;
    font-size: 13px;
    letter-spacing: 0.08em;
    line-height: 1.45;
    color: var(--ink-soft);
    white-space: nowrap;
  }

  /* Back: music staff + mark */
  .card--back {
    left: 590px;
    top: 410px;
  }

  .staff {
    position: absolute;
    inset: 0;
  }

  .brand {
    position: absolute;
    left: 54px;
    top: 157px;
    display: flex;
    align-items: center;
    gap: 12px;
    font-size: 40px;
    letter-spacing: 0.02em;
    line-height: 1;
    color: var(--ink);
  }

  .brand__dot {
    width: 14px;
    height: 14px;
    border-radius: 50%;
    background: var(--ink);
  }

  .back__name {
    position: absolute;
    right: 40px;
    top: 55px;
    margin: 0;
    font-size: 22px;
    font-weight: 500;
    line-height: 1.1;
    letter-spacing: 0.1em;
    text-transform: uppercase;
  }

  .back__role {
    position: absolute;
    right: 40px;
    top: 112px;
    font-size: 15px;
    line-height: 1.2;
    letter-spacing: 0.1em;
    text-transform: uppercase;
    color: var(--ink-soft);
  }
</style>
</head>
<body>
<main class="canvas">

  <section class="card card--front">
    <div class="portrait" role="img" aria-label="Photo of the violinist in a long black dress holding her violin against a stone wall"></div>
    <div class="contact">
      <h1 class="contact__name">Your Name Here</h1>
      <div class="contact__role">Violinist</div>
      <div class="contact__rule"></div>
      <ul class="contact__list">
        <li>214-555-0187</li>
        <li>hello@velastringstudio.com</li>
        <li>www.velastringstudio.com</li>
      </ul>
    </div>
  </section>

  <section class="card card--back">
    <svg class="staff" width="525" height="300" viewBox="0 0 525 300" aria-hidden="true">
      <g stroke="var(--staff-line)" stroke-width="1.2">
        <line x1="0" y1="40" x2="525" y2="40"/>
        <line x1="0" y1="95" x2="525" y2="95"/>
        <line x1="0" y1="150" x2="525" y2="150"/>
        <line x1="0" y1="205" x2="525" y2="205"/>
        <line x1="0" y1="260" x2="525" y2="260"/>
      </g>
    </svg>
    <div class="brand"><span class="brand__dot"></span>Vela Strings</div>
    <h2 class="back__name">Your Name Here</h2>
    <div class="back__role">Violinist</div>
  </section>

</main>
</body>
</html>
```